Professional Services (B-2-B) Business Cards (Front & Back)

Corvantis is a business-to-business professional services company in the legal sector. They typically present to c-suite and executive functions who are looking for providers with expertise, and experience. Our business card should look and feel professional and contemporary, but we are not a startup tech company, so we want the tone to be more mature.

```html
<!DOCTYPE html>
<html lang="en">
<head>
<meta charset="UTF-8">
<title>Corvantis Business Cards</title>
<link rel="stylesheet" href="https://fonts.googleapis.com/css2?family=Montserrat:wght@400;500&display=swap">
<style>
  :root {
    --backdrop: #e9eaec;
    --navy: #0c1f45;
    --navy-deep: #08183a;
    --navy-emboss: #1a2d55;
    --paper: #ffffff;
    --ink: #13254c;
    --rule: #13254c;
  }
  * { box-sizing: border-box; margin: 0; padding: 0; }
  html, body {
    width: 1200px;
    height: 801px;
    overflow: hidden;
    background: var(--backdrop);
    font-family: "Montserrat", sans-serif;
  }
  .sheet {
    width: 1200px;
    height: 801px;
    display: flex;
    align-items: center;
    justify-content: center;
    gap: 40px;
  }
  .card {
    width: 540px;
    height: 310px;
    position: relative;
    box-shadow: 0 6px 18px rgba(0,0,0,0.12);
  }
  .card--back {
    background: linear-gradient(160deg, var(--navy) 0%, var(--navy-deep) 100%);
    display: flex;
    align-items: center;
    justify-content: center;
    gap: 18px;
  }
  .card--back .brand-mark {
    width: 22px;
    height: 22px;
    background: var(--navy-emboss);
  }
  .card--back .brand-name {
    color: var(--navy-emboss);
    font-weight: 400;
    font-size: 26px;
    letter-spacing: 10px;
    text-transform: uppercase;
  }
  .card--front {
    background: var(--paper);
    color: var(--ink);
  }
  .front-brand {
    position: absolute;
    left: 40px;
    top: 58px;
    display: flex;
    align-items: center;
    gap: 16px;
  }
  .front-brand .brand-mark {
    width: 18px;
    height: 18px;
    background: var(--ink);
  }
  .front-brand .brand-name {
    font-weight: 400;
    font-size: 20px;
    letter-spacing: 8px;
    text-transform: uppercase;
    color: var(--ink);
  }
  .contact-block {
    position: absolute;
    left: 40px;
    top: 128px;
  }
  .person-name {
    font-weight: 500;
    font-size: 21px;
    letter-spacing: 1.5px;
    text-transform: uppercase;
  }
  .person-title {
    font-size: 12.5px;
    margin-top: 2px;
  }
  .divider {
    width: 168px;
    height: 1px;
    background: var(--rule);
    margin: 8px 0 8px;
  }
  .contact-list { list-style: none; }
  .contact-list li {
    display: flex;
    align-items: center;
    gap: 8px;
    font-size: 13px;
    line-height: 21px;
  }
  .contact-list svg {
    width: 12px;
    height: 12px;
    flex: none;
    fill: var(--ink);
  }
</style>
</head>
<body>
  <main class="sheet">
    <section class="card card--back" aria-label="Card back">
      <span class="brand-mark" aria-hidden="true"></span>
      <span class="brand-name">Corvantis</span>
    </section>

    <section class="card card--front" aria-label="Card front">
      <div class="front-brand">
        <span class="brand-mark" aria-hidden="true"></span>
        <span class="brand-name">Corvantis</span>
      </div>

      <div class="contact-block">
        <h1 class="person-name">Elias Marlow</h1>
        <p class="person-title">President &amp; CEO</p>
        <div class="divider"></div>
        <ul class="contact-list">
          <li>
            <svg viewBox="0 0 24 24" aria-hidden="true"><path d="M6.6 10.8a15.2 15.2 0 0 0 6.6 6.6l2.2-2.2a1 1 0 0 1 1-.25 11.4 11.4 0 0 0 3.6.57 1 1 0 0 1 1 1V20a1 1 0 0 1-1 1A17 17 0 0 1 3 4a1 1 0 0 1 1-1h3.5a1 1 0 0 1 1 1c0 1.25.2 2.45.57 3.6a1 1 0 0 1-.25 1z"/></svg>
            <span>(415) 555 - 0182</span>
          </li>
          <li>
            <svg viewBox="0 0 24 24" aria-hidden="true"><path d="M7 1h10a2 2 0 0 1 2 2v18a2 2 0 0 1-2 2H7a2 2 0 0 1-2-2V3a2 2 0 0 1 2-2zm0 3v14h10V4zm5 15.5a1 1 0 1 0 0 2 1 1 0 0 0 0-2z"/></svg>
            <span>(203) 555 - 0147</span>
          </li>
          <li>
            <svg viewBox="0 0 24 24" aria-hidden="true"><path d="M2 5h20v14H2zm2 2v.5l8 5 8-5V7zm0 2.9V17h16V9.9l-8 5z"/></svg>
            <span>emarlow@corvantis.tech</span>
          </li>
          <li>
            <svg viewBox="0 0 24 24" aria-hidden="true"><path d="M12 2a10 10 0 1 0 0 20 10 10 0 0 0 0-20zm6.9 6h-3a15.6 15.6 0 0 0-1.4-3.6A8 8 0 0 1 18.9 8zM12 4a14 14 0 0 1 1.9 4h-3.8A14 14 0 0 1 12 4zM4.3 14a8 8 0 0 1 0-4h3.4a16.5 16.5 0 0 0 0 4zm.8 2h3a15.6 15.6 0 0 0 1.4 3.6A8 8 0 0 1 5.1 16zm3-8h-3a8 8 0 0 1 4.4-3.6A15.6 15.6 0 0 0 8.1 8zM12 20a14 14 0 0 1-1.9-4h3.8A14 14 0 0 1 12 20zm2.3-6H9.7a14.7 14.7 0 0 1 0-4h4.6a14.7 14.7 0 0 1 0 4zm.2 5.6a15.6 15.6 0 0 0 1.4-3.6h3a8 8 0 0 1-4.4 3.6zm1.8-5.6a16.5 16.5 0 0 0 0-4h3.4a8 8 0 0 1 0 4z"/></svg>
            <span>www.corvantis.tech</span>
          </li>
        </ul>
      </div>
    </section>
  </main>
</body>
</html>
```